Lantern Finch Coffee Company

Logo and coffee packaging design for a new coffee roasting company. Our plan is to small batch, craft roast coffee with $1 for each pound sold donated to non-profit rescue dog operations. Web address will be lanternfinchcoffee.com
Prefer a logo with a Jack Russell Terrier or similar dog.....like the little VBT dog or Pobbs on the sitcom Dunmore.
Ideally we would have one package/bag for all our coffees with a place to put a sticker for the type coffee (origin, roast style etc) and maybe a sticker for the back or side with the story of a specific rescue dog associated with that roast.
Would like some strong color science based designs to make our product pop on the shelf.

```html
<!DOCTYPE html>
<html lang="en">
<head>
<meta charset="utf-8">
<title>Lantern Finch Coffee – Packaging Labels</title>
<link rel="stylesheet" href="https://fonts.googleapis.com/css2?family=Oswald:wght@300;400;500&family=Roboto:wght@400;500&display=swap">
<style>
  :root {
    --canvas-bg: #ececec;
    --canvas-bg-edge: #cfcfcf;
    --label-orange: #f15a22;
    --espresso: #3b1a08;
    --espresso-soft: #5a2c12;
    --mustard: #d39a16;
    --lemon: #fff200;
    --title-gold: #e7b21b;
    --sticker-white: #ffffff;
    --body-text: #e9c9a8;
    --url-gold: #f2c12e;
  }
  * { box-sizing: border-box; margin: 0; padding: 0; }
  html, body { width: 1200px; height: 1000px; overflow: hidden; }
  body {
    position: relative;
    background: radial-gradient(ellipse at 55% 25%, #fafafa 0%, var(--canvas-bg) 45%, var(--canvas-bg-edge) 100%);
    font-family: "Roboto", Arial, sans-serif;
  }

  /* Brand mark, top right */
  .brand-mark {
    position: absolute; left: 740px; top: 80px;
    width: 230px; height: 230px;
    display: flex; align-items: center; justify-content: center;
  }
  .brand-mark__circle {
    position: absolute; inset: 0;
    border-radius: 50%;
    border: 10px solid var(--espresso-soft);
  }
  .brand-mark__name {
    position: relative;
    font-family: "Oswald", sans-serif; font-weight: 400;
    font-size: 26px; line-height: 1.15; letter-spacing: 1px;
    color: var(--espresso-soft); text-align: center; text-transform: uppercase;
  }

  /* Flat label */
  .label { position: absolute; display: flex; }
  .label--origin { left: 90px; top: 345px; }
  .label--roast { left: 450px; top: 470px; }

  .label__front {
    width: 290px; height: 460px;
    background: var(--label-orange);
    position: relative;
  }
  .label__side {
    width: 56px; height: 460px;
    background: var(--espresso);
    position: relative;
    padding: 60px 6px 0;
  }

  .label__brand {
    position: absolute; left: 95px; top: 28px;
    width: 100px; height: 100px;
    display: flex; align-items: center; justify-content: center;
  }
  .label__brand-circle {
    position: absolute; inset: 0; border-radius: 50%;
    border: 4px solid var(--espresso-soft);
  }
  .label__brand-name {
    position: relative;
    font-family: "Oswald", sans-serif; font-weight: 400;
    font-size: 12px; line-height: 1.15; text-align: center;
    color: var(--espresso-soft); text-transform: uppercase;
  }

  .label__cup {
    position: absolute; left: 85px; top: 145px;
    width: 120px; height: 180px;
    background: linear-gradient(180deg, rgba(59,26,8,0.08), rgba(59,26,8,0.2));
    border-radius: 12px;
  }

  .label__panel {
    position: absolute; left: 5px; top: 340px;
    width: 265px; height: 110px;
    background: var(--espresso);
    padding: 12px 14px 10px 52px;
  }
  .label__marker {
    position: absolute; left: 12px; top: 10px;
    width: 26px; height: 80px;
  }
  .label--origin .label__marker { background: var(--mustard); }
  .label--roast .label__marker { background: var(--lemon); }
  .label__title {
    font-family: "Oswald", sans-serif; font-weight: 300;
    font-size: 28px; line-height: 1; color: var(--title-gold);
  }
  .label--roast .label__title { color: var(--lemon); font-weight: 400; }
  .label__desc {
    margin-top: 8px;
    font-size: 7.5px; line-height: 1.35; color: var(--body-text);
  }
  .label__url {
    margin-top: 8px;
    font-size: 10px; font-weight: 500; color: var(--url-gold);
  }

  .label__side-title {
    font-family: "Oswald", sans-serif; font-weight: 400;
    font-size: 15px; color: var(--title-gold);
  }
  .label__side-text {
    margin-top: 6px;
    font-size: 5.5px; line-height: 1.4; color: var(--body-text);
  }
  .label__sticker {
    position: absolute; left: 6px; bottom: 70px;
    width: 44px; height: 60px;
    background: var(--sticker-white);
  }
</style>
</head>
<body>

  <div class="brand-mark">
    <div class="brand-mark__circle"></div>
    <div class="brand-mark__name">Lantern Finch<br>Coffee</div>
  </div>

  <section class="label label--origin">
    <div class="label__front">
      <div class="label__brand">
        <div class="label__brand-circle"></div>
        <div class="label__brand-name">Lantern Finch<br>Coffee</div>
      </div>
      <div class="label__cup" role="img" aria-label="Illustration of a steaming coffee cup with a heart in the swirl of steam"></div>
      <div class="label__panel">
        <div class="label__marker"></div>
        <h2 class="label__title">ORIGIN</h2>
        <p class="label__desc">Small batch roasted for a rich, deliciously smooth body. Perfect anytime you want to enjoy a velvety, full cup of coffee.</p>
        <p class="label__url">lanternfinchcoffee.com</p>
      </div>
    </div>
    <div class="label__side">
      <h3 class="label__side-title">ORIGIN</h3>
      <p class="label__side-text">Small batch roast, bright and smooth, with notes of cocoa and cherry.</p>
      <div class="label__sticker"></div>
    </div>
  </section>

  <section class="label label--roast">
    <div class="label__front">
      <div class="label__brand">
        <div class="label__brand-circle"></div>
        <div class="label__brand-name">Lantern Finch<br>Coffee</div>
      </div>
      <div class="label__cup" role="img" aria-label="Illustration of a steaming coffee cup with a heart in the swirl of steam"></div>
      <div class="label__panel">
        <div class="label__marker"></div>
        <h2 class="label__title">ROAST</h2>
        <p class="label__desc">Small batch roasted for a rich, deliciously smooth body. Perfect anytime you want to enjoy a velvety, full cup of coffee.</p>
        <p class="label__url">lanternfinchcoffee.com</p>
      </div>
    </div>
    <div class="label__side">
      <h3 class="label__side-title">ORIGIN</h3>
      <p class="label__side-text">Small batch roast, bright and smooth, with notes of cocoa and cherry.</p>
      <div class="label__sticker"></div>
    </div>
  </section>

</body>
</html>
```